Brindlewick Music Studio needs a promotional postcard design

We are looking for a postcard design for a small business that provides clients with private music lesson instruction. We are looking for a design that will convey the message of "music is fun for kids" that will appeal to parents and encourage them to sign up. We have a company logo that should be used and our color scheme is teal and turquoise. All of our contact info should be displayed as well.

Target Market(s)

Parents with young kids

Contact Information for Business Card

web: www.brindlewickmusicstudio.example
email: lessons@brindlewickmusicstudio.example
phone: 202-555-0147

Font styles to use
Serif
Sans Serif

Colors
33b8a4
86cfc6
0456a4
87cfc6

Requirements
Must have
• Music lessons in your home
• Creating little stars one at a time
• Sign Up Now
• Please use these images:
Nice to have
• Something like this sample postcard:

```html
<!DOCTYPE html>
<html lang="en">
<head>
<meta charset="utf-8">
<title>Brindlewick Music Studio – Postcard</title>
<link rel="stylesheet" href="https://fonts.googleapis.com/css2?family=PT+Serif&family=Montserrat:wght@600;700&family=Roboto+Condensed:wght@400;700&display=swap">
<style>
  :root {
    --teal: #33b8a4;
    --turquoise: #4fbfbd;
    --teal-light: #86cfc6;
    --royal-blue: #0456a4;
    --royal-blue-dark: #033f82;
    --ink: #444b52;
    --paper: #ffffff;
    --paper-tint: #f2f4f5;
    --backdrop: #e7e9ea;
  }
  html, body {
    margin: 0;
    padding: 0;
    width: 870px;
    height: 1200px;
    overflow: hidden;
    background: var(--backdrop);
  }
  .postcard {
    position: absolute;
    left: 35px;
    top: 332px;
    width: 800px;
    height: 536px;
    box-shadow: 0 10px 30px rgba(0,0,0,.18);
  }
  .postcard svg { display: block; }
  .brand-name {
    font-family: "PT Serif", serif;
    font-size: 29px;
    fill: var(--teal);
  }
  .headline-serif {
    font-family: "PT Serif", serif;
    font-size: 36px;
    fill: var(--paper);
  }
  .headline-sans {
    font-family: "Montserrat", sans-serif;
    font-weight: 700;
    font-size: 28px;
    fill: var(--paper);
  }
  .tagline-small {
    font-family: "Montserrat", sans-serif;
    font-weight: 600;
    font-size: 17px;
    fill: var(--paper);
  }
  .tagline-large {
    font-family: "Roboto Condensed", sans-serif;
    font-weight: 700;
    font-size: 37px;
    fill: var(--paper);
  }
  .phone {
    font-family: "Roboto Condensed", sans-serif;
    font-weight: 700;
    font-size: 41px;
    fill: var(--teal);
  }
  .email {
    font-family: "Roboto Condensed", sans-serif;
    font-weight: 400;
    font-size: 14px;
    fill: var(--ink);
  }
  .cta-label {
    font-family: "Montserrat", sans-serif;
    font-weight: 700;
    font-size: 22px;
    fill: var(--paper);
  }
  .website {
    font-family: "Roboto Condensed", sans-serif;
    font-weight: 400;
    font-size: 18px;
    fill: var(--paper);
  }
</style>
</head>
<body>
<div class="postcard">
  <svg width="800" height="536" viewBox="0 0 800 536" xmlns="http://www.w3.org/2000/svg">
    <defs>
      <linearGradient id="paper-fade" x1="0" y1="0" x2="0" y2="1">
        <stop offset="0" stop-color="#eef1f2"/>
        <stop offset="1" stop-color="#ffffff"/>
      </linearGradient>
      <radialGradient id="hero-tone" cx="0.6" cy="0.35" r="0.75">
        <stop offset="0" stop-color="#c9a57e"/>
        <stop offset="0.45" stop-color="#9a7451"/>
        <stop offset="0.8" stop-color="#5e4431"/>
        <stop offset="1" stop-color="#3b2c24"/>
      </radialGradient>
      <linearGradient id="hero-lower" x1="0" y1="0" x2="0" y2="1">
        <stop offset="0" stop-color="#1f2230" stop-opacity="0"/>
        <stop offset="0.55" stop-color="#1f2230" stop-opacity="0.55"/>
        <stop offset="1" stop-color="#1b1d28" stop-opacity="0.85"/>
      </linearGradient>
      <radialGradient id="tone-home" cx="0.45" cy="0.4" r="0.7">
        <stop offset="0" stop-color="#d9cfc4"/>
        <stop offset="0.6" stop-color="#8c7a6e"/>
        <stop offset="1" stop-color="#3e3f63"/>
      </radialGradient>
      <radialGradient id="tone-stage-group" cx="0.5" cy="0.6" r="0.7">
        <stop offset="0" stop-color="#b98a7c"/>
        <stop offset="0.55" stop-color="#4b4a66"/>
        <stop offset="1" stop-color="#15161d"/>
      </radialGradient>
      <radialGradient id="tone-recital" cx="0.55" cy="0.55" r="0.7">
        <stop offset="0" stop-color="#c23a2e"/>
        <stop offset="0.5" stop-color="#8a4a2a"/>
        <stop offset="1" stop-color="#3a2016"/>
      </radialGradient>
      <radialGradient id="tone-violinist" cx="0.5" cy="0.5" r="0.6">
        <stop offset="0" stop-color="#a98774"/>
        <stop offset="0.5" stop-color="#3a2e2c"/>
        <stop offset="1" stop-color="#0f0f12"/>
      </radialGradient>
      <linearGradient id="button-fill" x1="0" y1="0" x2="0" y2="1">
        <stop offset="0" stop-color="#1a6fc0"/>
        <stop offset="1" stop-color="var(--royal-blue-dark)"/>
      </linearGradient>
      <linearGradient id="band-fill" x1="0" y1="0" x2="1" y2="0">
        <stop offset="0" stop-color="var(--teal)"/>
        <stop offset="1" stop-color="var(--turquoise)"/>
      </linearGradient>
    </defs>

    <rect class="card-base" width="800" height="536" fill="url(#paper-fade)"/>

    <!-- hero photo area -->
    <g class="hero-photo" role="img" aria-label="Photo of a smiling young girl making a peace sign">
      <path d="M432 0 Q478 220 428 536 H800 V0 Z" fill="url(#hero-tone)"/>
      <path d="M432 0 Q478 220 428 536 H800 V0 Z" fill="url(#hero-lower)"/>
    </g>
    <path class="hero-accent" d="M398 0 Q446 30 468 118 L458 120 Q440 40 388 0 Z" fill="var(--royal-blue)"/>
    <path class="hero-accent-lower" d="M430 470 Q446 500 452 536 L444 536 Q440 505 424 474 Z" fill="var(--teal-light)"/>

    <!-- brand -->
    <circle class="brand-mark" cx="135" cy="59" r="36" fill="var(--teal)"/>
    <text class="brand-name" x="186" y="52">Brindlewick</text>
    <text class="brand-name" x="186" y="86">Music Studio</text>

    <!-- headline band -->
    <rect class="headline-band" x="0" y="121" width="440" height="144" fill="url(#band-fill)"/>
    <text class="headline-serif" x="33" y="168">Music Lessons</text>
    <text class="headline-sans" x="33" y="204">IN YOUR HOME</text>

    <!-- tagline pill -->
    <path class="tagline-pill" d="M0 228 H252 A39 39 0 0 1 252 306 H0 Z" fill="var(--royal-blue)"/>
    <text class="tagline-small" x="30" y="256">CREATING LITTLE STARS</text>
    <text class="tagline-large" x="30" y="294">ONE AT A TIME</text>

    <!-- contact -->
    <text class="phone" x="31" y="370">202-555-0147</text>
    <g class="email-icon" transform="translate(33 386)">
      <rect width="15" height="10" fill="var(--teal)"/>
      <path d="M0 0 L7.5 5.5 L15 0" fill="none" stroke="var(--paper)" stroke-width="1.5"/>
    </g>
    <text class="email" x="55" y="396">lessons@brindlewickmusicstudio.example</text>

    <!-- call to action -->
    <rect class="cta-button" x="29" y="417" width="248" height="49" rx="4" fill="url(#button-fill)"/>
    <text class="cta-label" x="44" y="450">SIGN UP NOW</text>
    <circle cx="248" cy="441" r="11" fill="var(--paper)"/>
    <path d="M243 436 L248 441 L243 446 Z M248 436 L253 441 L248 446 Z" fill="var(--royal-blue)"/>

    <!-- footer bar -->
    <path class="footer-bar" d="M0 491 H400 Q430 505 440 536 H0 Z" fill="var(--royal-blue)"/>
    <g class="globe-icon" transform="translate(40 514)" fill="none" stroke="var(--paper)" stroke-width="1.4">
      <circle r="8"/>
      <ellipse rx="3.5" ry="8"/>
      <line x1="-8" y1="0" x2="8" y2="0"/>
    </g>
    <text class="website" x="56" y="520">www.brindlewickmusicstudio.example</text>

    <!-- activity photo circles -->
    <g class="activity-photos" stroke="var(--paper)" stroke-width="6">
      <circle cx="424" cy="123" r="52" fill="url(#tone-home)" role="img" aria-label="Photo of a child playing violin at home"/>
      <circle cx="388" cy="225" r="55" fill="url(#tone-stage-group)" role="img" aria-label="Photo of a group of children performing on stage"/>
      <circle cx="368" cy="334" r="53" fill="url(#tone-recital)" role="img" aria-label="Photo of a child performing at a recital"/>
      <circle cx="382" cy="441" r="55" fill="url(#tone-violinist)" role="img" aria-label="Photo of a young violinist on stage"/>
    </g>
  </svg>
</div>
</body>
</html>
```